ORVA MELKANTE - LUXURY RESORT CORVAL HOTEL

We wanna promote the luxury hotel based on marroquian stylish luxury decor, it is still a project but we need to expose it.
Houses will be A frame type houses surrounded by florest and water dumps - please check - odeleite amber heron at google to check localisation
Container luxury houses also will be included heaven blue velvet and green and rose gold are the Color. The sky is the limit.

```html
<!DOCTYPE html>
<html lang="en">
<head>
<meta charset="utf-8">
<title>Orva Melkante Stationery</title>
<link href="https://fonts.googleapis.com/css2?family=Cormorant+Garamond:wght@400&family=Oswald:wght@400&family=PT+Sans:wght@400;700&display=swap" rel="stylesheet">
<style>
  :root {
    --backdrop: #aba9aa;
    --paper: #f6f3f3;
    --tan: #c49a6c;
    --ink: #474747;
    --ink-soft: #5a5a5a;
    --white: #ffffff;
  }
  * { margin: 0; padding: 0; box-sizing: border-box; }
  html, body { width: 1200px; height: 770px; overflow: hidden; }
  body { background: var(--backdrop); position: relative; font-family: "PT Sans", sans-serif; }

  .sheet { position: absolute; background: var(--paper); box-shadow: 0 2px 8px rgba(0,0,0,0.28); }

  .brand-name {
    position: absolute;
    font-family: "Cormorant Garamond", serif;
    font-weight: 400;
    color: var(--tan);
    letter-spacing: 0.16em;
    text-transform: uppercase;
    white-space: nowrap;
  }

  .contact-band {
    position: absolute; left: 0; right: 0;
    background: var(--tan);
    color: var(--white);
    font-family: "Oswald", sans-serif;
    font-weight: 400;
    white-space: nowrap;
    display: flex; align-items: center;
  }

  /* Envelope front */
  .envelope-front { left: 61px; top: 203px; width: 560px; height: 254px; }
  .envelope-front .brand-name { left: 34px; top: 28px; font-size: 18px; }
  .envelope-front .contact-band { top: 200px; height: 23px; padding-left: 33px; font-size: 10.5px; right: -1px; }

  /* Envelope back */
  .envelope-back { left: 57px; top: 480px; width: 558px; height: 253px; }
  .envelope-flap { position: absolute; left: 0; top: 0; width: 558px; height: 93px; display: block; }

  /* Letterhead */
  .letterhead { left: 643px; top: 33px; width: 496px; height: 701px; }
  .letterhead .brand-name { left: 124px; top: 60px; font-size: 25px; }
  .letter-date { position: absolute; left: 48px; top: 177px; font-size: 9.5px; font-weight: 700; color: var(--ink); }
  .recipient { position: absolute; left: 48px; top: 213px; font-size: 9.5px; line-height: 12px; font-weight: 700; color: var(--ink); font-style: normal; }
  .letter-body { position: absolute; left: 47px; top: 283px; width: 401px; font-size: 7.4px; line-height: 12px; color: var(--ink-soft); text-align: justify; }
  .letter-body p + p { margin-top: 12px; }
  .signature { position: absolute; left: 356px; top: 528px; width: 81px; height: 33px; background: linear-gradient(90deg, rgba(40,40,40,0.08), rgba(40,40,40,0.18)); }
  .signer-role { position: absolute; left: 377px; top: 558px; font-size: 8px; color: var(--ink); }
  .letterhead .contact-band { top: 647px; height: 23px; justify-content: center; font-size: 10px; }
</style>
</head>
<body>

  <section class="sheet envelope-front">
    <div class="brand-name">Orva Melkante</div>
    <div class="contact-band">Velmora - Eastbank Dunmere</div>
  </section>

  <section class="sheet envelope-back">
    <svg class="envelope-flap" viewBox="0 0 558 93" aria-hidden="true">
      <path d="M0 0 H558 L547 66 Q542 93 512 93 H46 Q16 93 11 66 Z" fill="var(--tan)"/>
    </svg>
  </section>

  <section class="sheet letterhead">
    <div class="brand-name">Orva Melkante</div>
    <div class="letter-date">Portvella, Ocober 12,2015</div>
    <address class="recipient">Sr.<br>TOMAS ARRENDI<br>Web Master<br>City</address>
    <div class="letter-body">
      <p>Contrary to popular belief, Lorem Ipsum is not simply random text. It has roots in a piece of classical Latin literature from 45 BC, making it over 2000 years old. Edwin Marlow, a Latin professor at Ashcombe College in Carrowshire, looked up one of the more obscure Latin words, consectetur, from a Lorem Ipsum passage, and going through the cites of the word in classical literature,</p>
      <p>discovered the undoubtable source. Lorem Ipsum comes from sections 1.10.32 and 1.10.33 of "de Finibus Bonorum et Malorum" (The Extremes of Good and Evil) by Varenus, written in 45 BC. This book is a treatise on the theory of ethics, very popular during the Renaissance. The first line of Lorem Ipsum, "Lorem ipsum dolor sit amet..", comes from a line in section 1.10.32.</p>
      <p>The standard chunk of Lorem Ipsum used since the 1500s is reproduced below for those interested. Sections 1.10.32 and 1.10.33 from "de Finibus Bonorum et Malorum" by Varenus are also reproduced in their exact original form, accompanied by English versions from the 1914 translation by H. Dallow.</p>
      <p>There are many variations of passages of Lorem Ipsum available, but the majority have suffered alteration in some form, by injected humour, or randomised words which don't look even slightly believable. If you are going to use a passage of Lorem Ipsum, you need to be sure there isn't anything embarrassing hidden in the middle of text. All the Lorem Ipsum generators o</p>
    </div>
    <div class="signature" role="img" aria-label="Handwritten signature of the founder"></div>
    <div class="signer-role">CEO/ FOUNDER</div>
    <div class="contact-band">Velmora - Eastbank Dunmere | P. +00 0x xxxx xxxx E. Nadia.Ferrow@velquiro.com W. www.velquiro.com</div>
  </section>

</body>
</html>
```